Packaging Design for "Out-along" healthy snack

We are a young trading company based in Melaka, Malaysia. Our product range include healthy snack food products such as;
1. Dried fruit (Raisin, Date and Apricot)
2. Nuts (Almond, walnut and Pitstachio)

Our Brand name is - Out-Along (registrated mark)
Motto: Healthy snacks that everyone will craved out-along meal time.

Target market segment:
1. Night life business such as Pub, Lounge, Kara-oke
2. Vegetarian and Health food restaurant
3. Appetiser for Premium Restaurant

Packs size : 100g, 250g and 500g

Packing type: Screw Cap Jar (Square L7.5cm X W7.5cm X H9.0cm)

Competitor website:
http://www.plakorvanel.example/index.php?ws=ourproducts&cat=Nuts#openproducts

https://grivoltasp.example/driedfruit/ (For company philosophy)

KMTarvu
kelbrimo@quadrelmail.example

Vorelix Tarn (M) Sdn. Bhd. (owner of Out-along brand)

Target Market(s)

Customer that have middle and high income that have disposable budget for healthy and good taste snack in between meal time. Those business man that like to meet client at the night life outlets would enjoy our snacks

Industry/Entity Type

It Company

Font styles to use
Sans Serif

Colors
faa54b
886aae
87cfc6

Requirements
Must have
• 1. Out-along as brand name
• 2. Product names area
• 3. Die cut window that let consumer see the product inside
• 4. Nutritional facts and Ingredients
Nice to have
• 1. A attractive logo for "Out-along" brand

```html
<!DOCTYPE html>
<html lang="en">
<head>
<meta charset="utf-8">
<title>Out-Along Premium Mixed Nuts — Label Range</title>
<link href="https://fonts.googleapis.com/css2?family=Bebas+Neue&family=Oswald:wght@400;500&display=swap" rel="stylesheet">
<style>
  :root {
    --page: #ffffff;
    --ink: #111111;
    --paper: #ffffff;
    --purple: #886aae;
    --orange: #faa54b;
    --teal: #87cfc6;
    --nut-dark: #7a3f22;
    --nut-mid: #a8643a;
    --nut-light: #dcc4a2;
  }
  * { margin: 0; padding: 0; box-sizing: border-box; }
  html, body { width: 1000px; height: 1200px; overflow: hidden; background: var(--page); }
  .canvas { position: relative; width: 1000px; height: 1200px; }

  .label { position: absolute; width: 350px; height: 370px; overflow: hidden; }
  .label--purple { left: 90px; top: 160px; --band: var(--purple); --text: var(--ink); --badge: var(--ink); --badge-text: var(--paper); }
  .label--orange { left: 560px; top: 160px; --band: var(--orange); --text: var(--ink); --badge: var(--ink); --badge-text: var(--paper); }
  .label--black  { left: 90px; top: 750px; --band: var(--ink); --text: var(--paper); --badge: var(--paper); --badge-text: var(--ink); }
  .label--teal   { left: 560px; top: 750px; --band: var(--teal); --text: var(--ink); --badge: var(--ink); --badge-text: var(--paper); }

  .window {
    position: absolute; inset: 0;
    background: linear-gradient(160deg, var(--nut-mid) 0%, var(--nut-light) 35%, var(--nut-dark) 60%, var(--nut-light) 80%, var(--nut-mid) 100%);
  }
  .artwork { position: absolute; inset: 0; width: 350px; height: 370px; }
  .band { fill: var(--band); }
  .brand-name { fill: var(--text); font-family: "Oswald", sans-serif; font-size: 20px; font-weight: 500; letter-spacing: 0.5px; }
  .kicker { fill: var(--text); font-family: "Oswald", sans-serif; font-size: 8px; font-weight: 500; letter-spacing: 3px; }
  .rule { stroke: var(--text); stroke-width: 1; }
  .product-name { fill: var(--text); font-family: "Bebas Neue", sans-serif; font-size: 46px; letter-spacing: 4px; }
  .tagline { fill: var(--text); font-family: "Oswald", sans-serif; font-size: 8.5px; font-weight: 500; }
  .quote-mark { fill: var(--text); font-family: "Oswald", sans-serif; font-size: 18px; font-weight: 500; }
  .badge { fill: var(--badge); }
  .badge-text { fill: var(--badge-text); font-family: "Oswald", sans-serif; font-size: 7px; font-weight: 500; }
  .weight { fill: var(--text); font-family: "Oswald", sans-serif; font-size: 9px; font-weight: 500; }
</style>
</head>
<body>
<main class="canvas">

  <section class="label label--purple">
    <div class="window" role="img" aria-label="Die-cut window showing cashews, almonds, hazelnuts and peanuts inside the jar"></div>
    <svg class="artwork" viewBox="0 0 350 370" aria-label="Out-Along Premium Mixed Nuts label">
      <polygon class="band" points="0,28 350,130 350,280 0,185"/>
      <polygon class="band" points="0,295 240,370 0,370"/>
      <text class="brand-name" x="6" y="96">Out-Along</text>
      <line class="rule" x1="95" y1="137" x2="145" y2="137"/>
      <text class="kicker" x="183" y="140" text-anchor="middle">PREMIUM</text>
      <line class="rule" x1="220" y1="137" x2="270" y2="137"/>
      <text class="product-name" x="183" y="183" text-anchor="middle">MIXED NUTS</text>
      <text class="quote-mark" x="194" y="214">'</text>
      <text class="tagline" x="200" y="212">THE HEALTHY SNACK</text>
      <text class="tagline" x="200" y="225">THAT EVERYONE CRAVES</text>
      <text class="tagline" x="200" y="238">OUT-ALONG MEAL TIME</text>
      <circle class="badge" cx="17" cy="340" r="13"/>
      <text class="badge-text" x="17" y="338" text-anchor="middle">HEA</text><text class="badge-text" x="17" y="346" text-anchor="middle">LTHY</text>
      <circle class="badge" cx="49" cy="340" r="13"/>
      <text class="badge-text" x="49" y="338" text-anchor="middle">NAT</text><text class="badge-text" x="49" y="346" text-anchor="middle">URAL</text>
      <circle class="badge" cx="81" cy="340" r="13"/>
      <text class="badge-text" x="81" y="338" text-anchor="middle">ORG</text><text class="badge-text" x="81" y="346" text-anchor="middle">ANIC</text>
      <text class="weight" x="122" y="353">500G</text>
    </svg>
  </section>

  <section class="label label--orange">
    <div class="window" role="img" aria-label="Die-cut window showing cashews, almonds, hazelnuts and peanuts inside the jar"></div>
    <svg class="artwork" viewBox="0 0 350 370" aria-label="Out-Along Premium Mixed Nuts label">
      <polygon class="band" points="0,28 350,130 350,280 0,185"/>
      <polygon class="band" points="0,295 240,370 0,370"/>
      <text class="brand-name" x="6" y="96">Out-Along</text>
      <line class="rule" x1="95" y1="137" x2="145" y2="137"/>
      <text class="kicker" x="183" y="140" text-anchor="middle">PREMIUM</text>
      <line class="rule" x1="220" y1="137" x2="270" y2="137"/>
      <text class="product-name" x="183" y="183" text-anchor="middle">MIXED NUTS</text>
      <text class="quote-mark" x="194" y="214">'</text>
      <text class="tagline" x="200" y="212">THE HEALTHY SNACK</text>
      <text class="tagline" x="200" y="225">THAT EVERYONE CRAVES</text>
      <text class="tagline" x="200" y="238">OUT-ALONG MEAL TIME</text>
      <circle class="badge" cx="17" cy="340" r="13"/>
      <text class="badge-text" x="17" y="338" text-anchor="middle">HEA</text><text class="badge-text" x="17" y="346" text-anchor="middle">LTHY</text>
      <circle class="badge" cx="49" cy="340" r="13"/>
      <text class="badge-text" x="49" y="338" text-anchor="middle">NAT</text><text class="badge-text" x="49" y="346" text-anchor="middle">URAL</text>
      <circle class="badge" cx="81" cy="340" r="13"/>
      <text class="badge-text" x="81" y="338" text-anchor="middle">ORG</text><text class="badge-text" x="81" y="346" text-anchor="middle">ANIC</text>
      <text class="weight" x="122" y="353">500G</text>
    </svg>
  </section>

  <section class="label label--black">
    <div class="window" role="img" aria-label="Die-cut window showing cashews, almonds, hazelnuts and peanuts inside the jar"></div>
    <svg class="artwork" viewBox="0 0 350 370" aria-label="Out-Along Premium Mixed Nuts label">
      <polygon class="band" points="0,28 350,130 350,280 0,185"/>
      <polygon class="band" points="0,295 240,370 0,370"/>
      <text class="brand-name" x="6" y="96">Out-Along</text>
      <line class="rule" x1="95" y1="137" x2="145" y2="137"/>
      <text class="kicker" x="183" y="140" text-anchor="middle">PREMIUM</text>
      <line class="rule" x1="220" y1="137" x2="270" y2="137"/>
      <text class="product-name" x="183" y="183" text-anchor="middle">MIXED NUTS</text>
      <text class="quote-mark" x="194" y="214">'</text>
      <text class="tagline" x="200" y="212">THE HEALTHY SNACK</text>
      <text class="tagline" x="200" y="225">THAT EVERYONE CRAVES</text>
      <text class="tagline" x="200" y="238">OUT-ALONG MEAL TIME</text>
      <circle class="badge" cx="17" cy="340" r="13"/>
      <text class="badge-text" x="17" y="338" text-anchor="middle">HEA</text><text class="badge-text" x="17" y="346" text-anchor="middle">LTHY</text>
      <circle class="badge" cx="49" cy="340" r="13"/>
      <text class="badge-text" x="49" y="338" text-anchor="middle">NAT</text><text class="badge-text" x="49" y="346" text-anchor="middle">URAL</text>
      <circle class="badge" cx="81" cy="340" r="13"/>
      <text class="badge-text" x="81" y="338" text-anchor="middle">ORG</text><text class="badge-text" x="81" y="346" text-anchor="middle">ANIC</text>
      <text class="weight" x="122" y="353">500G</text>
    </svg>
  </section>

  <section class="label label--teal">
    <div class="window" role="img" aria-label="Die-cut window showing cashews, almonds, hazelnuts and peanuts inside the jar"></div>
    <svg class="artwork" viewBox="0 0 350 370" aria-label="Out-Along Premium Mixed Nuts label">
      <polygon class="band" points="0,28 350,130 350,280 0,185"/>
      <polygon class="band" points="0,295 240,370 0,370"/>
      <text class="brand-name" x="6" y="96">Out-Along</text>
      <line class="rule" x1="95" y1="137" x2="145" y2="137"/>
      <text class="kicker" x="183" y="140" text-anchor="middle">PREMIUM</text>
      <line class="rule" x1="220" y1="137" x2="270" y2="137"/>
      <text class="product-name" x="183" y="183" text-anchor="middle">MIXED NUTS</text>
      <text class="quote-mark" x="194" y="214">'</text>
      <text class="tagline" x="200" y="212">THE HEALTHY SNACK</text>
      <text class="tagline" x="200" y="225">THAT EVERYONE CRAVES</text>
      <text class="tagline" x="200" y="238">OUT-ALONG MEAL TIME</text>
      <circle class="badge" cx="17" cy="340" r="13"/>
      <text class="badge-text" x="17" y="338" text-anchor="middle">HEA</text><text class="badge-text" x="17" y="346" text-anchor="middle">LTHY</text>
      <circle class="badge" cx="49" cy="340" r="13"/>
      <text class="badge-text" x="49" y="338" text-anchor="middle">NAT</text><text class="badge-text" x="49" y="346" text-anchor="middle">URAL</text>
      <circle class="badge" cx="81" cy="340" r="13"/>
      <text class="badge-text" x="81" y="338" text-anchor="middle">ORG</text><text class="badge-text" x="81" y="346" text-anchor="middle">ANIC</text>
      <text class="weight" x="122" y="353">500G</text>
    </svg>
  </section>

</main>
</body>
</html>
```